Legislative compliance to home owners, landlords and agents

Logo, business card and stationaly header for a sole trader offering sevices in the UK to home owners, landlords and Letting agents to meet legislation requirement relating to sale and leasing of rental domestic homes. Services offered include Legionella Risk Assessment, Portable Appliance Testing and Energy Performance Certificates. Logo to include depiction of a house and compliance tick list images. Have an existing card with water splash image to reflect water testing, so considering picking up same wave blue. Company name Talvane Property Services. Web www.talvaneps-example.com. email: info@talvaneps-example.com. Address: Glenmorrow, Aberdeen. All three services to be listed. Name as existing card.,

Target Market(s)

UK home owners, landlords, lettings and estate agents

Industry/Entity Type

Property Management

Contact Information for Business Card

Derek Hollingsby CEng, MSoHTF
Address: Glenmorrow, Aberdeen
Web: www.talvaneps-example.com
e-mail info@talvaneps-example.com
Phone: 07921 458 302
Services: Legionella Risk Assessment, Portable Appliance Testing, Energy Performance Certificate

Logo Text

Talvane Property Services

Font styles to use
Sans Serif

Colors

Designer to choose colors to be used in the design.

Requirements
Must have
• Suitable for standard UK business card size 85 mm x 55 mm, with allowance for safety border/ bleed such that colours extend to outside border of card once printed
Nice to have
• Clear font style and layout
• Happy to see images depicting phone, address etc

```html
<!DOCTYPE html>
<html lang="en">
<head>
<meta charset="utf-8">
<title>Talvane Property Services – Business Card</title>
<link rel="stylesheet" href="https://fonts.googleapis.com/css2?family=Lato:wght@400;700;900&display=swap">
<style>
  :root {
    --stage: #2b2b2d;
    --card-white: #ffffff;
    --card-mist: #e9e9ec;
    --navy: #0b0e6b;
    --navy-deep: #070a55;
    --wave-blue: #2a9fd8;
    --soft-white: #f2f3ff;
  }
  * { box-sizing: border-box; margin: 0; padding: 0; }
  html, body {
    width: 1200px; height: 997px; overflow: hidden;
    background: var(--stage);
    font-family: "Lato", sans-serif;
  }
  .card {
    position: absolute; left: 180px; top: 226px;
    width: 840px; height: 544px;
    border-radius: 22px; overflow: hidden;
    background: linear-gradient(180deg, var(--card-white) 0%, var(--card-mist) 44%);
    box-shadow: 0 18px 40px rgba(0,0,0,0.55);
  }
  .brand {
    position: absolute; left: 0; right: 0; top: 108px;
    display: flex; align-items: center; justify-content: center; gap: 14px;
  }
  .brand-dot {
    width: 22px; height: 22px; border-radius: 50%;
    background: var(--wave-blue);
  }
  .brand-name {
    font-weight: 900; font-size: 40px; color: var(--navy);
    letter-spacing: 0.3px;
  }
  .rule {
    position: absolute; left: 0; right: 0; top: 236px; height: 4px;
    background: var(--navy);
  }
  .band {
    position: absolute; left: 0; right: 0; top: 250px; height: 222px;
    background: linear-gradient(180deg, var(--navy) 0%, var(--navy-deep) 100%);
  }
  .notch {
    position: absolute; left: 62px; top: 0;
    width: 0; height: 0;
    border-left: 14px solid transparent; border-right: 14px solid transparent;
    border-top: 16px solid var(--wave-blue);
  }
  .person { position: absolute; left: 70px; top: 38px; }
  .person-name {
    color: var(--soft-white); font-weight: 700; font-size: 23px;
    text-transform: uppercase; letter-spacing: 0.4px;
    white-space: nowrap;
  }
  .person-role {
    color: var(--wave-blue); font-weight: 700; font-size: 18px;
    text-transform: uppercase; margin-top: 2px;
  }
  .contacts {
    position: absolute; left: 70px; top: 112px;
    list-style: none; display: flex; flex-direction: column; gap: 10px;
  }
  .contact {
    display: flex; align-items: center; gap: 12px;
    color: var(--soft-white); font-size: 19px;
  }
  .contact-icon {
    width: 22px; height: 22px; border-radius: 50%;
    background: var(--wave-blue);
    display: flex; align-items: center; justify-content: center;
  }
  .website {
    position: absolute; right: 48px; top: 176px;
    color: var(--wave-blue); font-weight: 700; font-size: 19px;
    letter-spacing: 2px; white-space: nowrap;
  }
  .services {
    position: absolute; left: 0; right: 0; top: 494px;
    display: flex; justify-content: center; gap: 18px;
    list-style: none;
    color: var(--navy); font-weight: 700; font-size: 18px;
  }
  .service::before {
    content: "•"; color: var(--wave-blue); margin-right: 6px;
  }
</style>
</head>
<body>
  <article class="card">
    <div class="brand">
      <span class="brand-dot"></span>
      <span class="brand-name">Talvane Property Services</span>
    </div>

    <div class="rule"></div>

    <section class="band">
      <span class="notch"></span>

      <div class="person">
        <p class="person-name">Derek Hollingsby CEng, MSoHTF</p>
        <p class="person-role">Director</p>
      </div>

      <ul class="contacts">
        <li class="contact">
          <span class="contact-icon">
            <svg width="12" height="12" viewBox="0 0 24 24"><path fill="#fff" d="M6.6 10.8a15 15 0 0 0 6.6 6.6l2.2-2.2c.3-.3.7-.4 1-.2 1.1.4 2.3.6 3.6.6.6 0 1 .4 1 1V20c0 .6-.4 1-1 1A17 17 0 0 1 3 4c0-.6.4-1 1-1h3.5c.6 0 1 .4 1 1 0 1.3.2 2.5.6 3.6.1.3 0 .7-.2 1z"/></svg>
          </span>
          07921 458 302
        </li>
        <li class="contact">
          <span class="contact-icon">
            <svg width="12" height="12" viewBox="0 0 24 24"><path fill="#fff" d="M3 5h18v14H3z"/><path fill="none" stroke="#2a9fd8" stroke-width="2" d="M3 6l9 7 9-7"/></svg>
          </span>
          info@talvaneps-example.com
        </li>
        <li class="contact">
          <span class="contact-icon">
            <svg width="12" height="12" viewBox="0 0 24 24"><path fill="#fff" d="M12 2a7 7 0 0 0-7 7c0 5 7 13 7 13s7-8 7-13a7 7 0 0 0-7-7zm0 9.5A2.5 2.5 0 1 1 12 6.5a2.5 2.5 0 0 1 0 5z"/></svg>
          </span>
          Glenmorrow, Aberdeen
        </li>
      </ul>

      <p class="website">www.talvaneps-example.com</p>
    </section>

    <ul class="services">
      <li class="service">Legionella Risk Assessment</li>
      <li class="service">Portable Appliance Testing</li>
      <li class="service">Energy Performance Certificates</li>
    </ul>
  </article>
</body>
</html>
```